Business Card Design Project

I would like to redesign our business cards and change the look and feel of our marketing material, but maintain the same basic identity of our current logo.
It is my belief that it could be much better.
You can view our website at kducn.com

   

I was looking for a completely different look.  Something much more hip and cool looking.  You can change the colors.

I like this look and feel

 http://www.hudlawfirm.com

 But obviously don’t want to copy them exactly.

 

For the back just leave the last point.

“Focus on Your Business, and We’ll Focus on Your Claim”

I want there to be space for someone to write on.

                                                                    

                                       

I like this look and feel

 http://www.hudlawfirm.com

```html
<!DOCTYPE html>
<html lang="en">
<head>
<meta charset="utf-8">
<title>Kducn Claim Partners – Business Card</title>
<link rel="stylesheet" href="https://fonts.googleapis.com/css2?family=Crimson+Text:wght@400;600&display=swap">
<style>
  :root {
    --gold-light: #d2a45c;
    --gold-mid: #a87a3a;
    --gold-dark: #5e4220;
    --blue-bright: #2f5fe6;
    --blue-mid: #1430c8;
    --blue-deep: #0a1a8c;
    --accent-orange: #f7931e;
    --brand-navy: #14237a;
    --mark-white: #f4f6f8;
  }
  html, body {
    margin: 0;
    padding: 0;
    width: 1200px;
    height: 691px;
    overflow: hidden;
    background: #ffffff;
  }
  .card {
    position: relative;
    width: 1200px;
    height: 691px;
    overflow: hidden;
    font-family: "Crimson Text", serif;
  }
  .card-background {
    position: absolute;
    inset: 0;
    display: block;
  }
  .brand {
    position: absolute;
    left: 23px;
    top: 42px;
    display: flex;
    align-items: center;
  }
  .brand-mark {
    width: 128px;
    height: 128px;
    border-radius: 50%;
    background: var(--mark-white);
    flex: none;
  }
  .brand-name {
    margin-left: 36px;
    color: var(--brand-navy);
    font-weight: 600;
    font-size: 36px;
    line-height: 56px;
    letter-spacing: 3px;
    text-transform: uppercase;
  }
  .contact {
    position: absolute;
    left: 747px;
    top: 222px;
    color: var(--accent-orange);
  }
  .contact-name {
    margin: 0;
    font-weight: 400;
    font-size: 46px;
    line-height: 52px;
    padding-bottom: 2px;
    border-bottom: 3px solid var(--accent-orange);
    display: inline-block;
    width: 317px;
  }
  .contact-details {
    margin: 16px 0 0;
    padding: 0;
    list-style: none;
    font-size: 30px;
    line-height: 44.8px;
  }
  .website {
    position: absolute;
    left: 146px;
    top: 636px;
    color: var(--accent-orange);
    font-size: 29px;
    line-height: 34px;
  }
</style>
</head>
<body>
  <div class="card">
    <svg class="card-background" width="1200" height="691" viewBox="0 0 1071 617" preserveAspectRatio="none" aria-hidden="true">
      <defs>
        <radialGradient id="gold-sheen" cx="0.5" cy="0.4" r="0.75">
          <stop offset="0" stop-color="var(--gold-light)" style="stop-color:#d2a45c"/>
          <stop offset="0.55" stop-color="#a87a3a"/>
          <stop offset="1" stop-color="#5e4220"/>
        </radialGradient>
        <radialGradient id="blue-glow" cx="0.35" cy="0.35" r="0.8">
          <stop offset="0" stop-color="#2f5fe6"/>
          <stop offset="0.5" stop-color="#1430c8"/>
          <stop offset="1" stop-color="#0a1a8c"/>
        </radialGradient>
      </defs>
      <rect class="gold-panel" width="1071" height="617" fill="url(#gold-sheen)"/>
      <path class="blue-sweep-rim" d="M688 0 C540 150 468 380 487 617 L1071 617 L1071 0 Z" fill="#e0a24a"/>
      <path class="blue-sweep" d="M693 0 C545 150 473 380 492 617 L1071 617 L1071 0 Z" fill="url(#blue-glow)"/>
    </svg>

    <div class="brand">
      <div class="brand-mark"></div>
      <div class="brand-name">Kducn Claim<br>Partners</div>
    </div>

    <div class="contact">
      <h1 class="contact-name">Daniel Marlowe</h1>
      <ul class="contact-details">
        <li>742 Harbor Avenue</li>
        <li>Westbury, NY 11590</li>
        <li>P : 516-555-0148</li>
        <li>M : 917-555-0172</li>
        <li>dm@kducn.com</li>
      </ul>
    </div>

    <div class="website">www.kducn.com</div>
  </div>
</body>
</html>
```